Poster for a series of live music events

Looking for a simplistic poster design for live music gigs. I would like something that i can reuse by moving the positioning of the words on the poster and the colour scheme. Attached is an example of a design that i like. The size should be A4.
File format preferred would be photoshop.
Text in the poster is not that important at this stage as it is just a template i am after. But it should include band names, location, date and time. So feel free to make up the text. The file provided in the brief will show you the similar things that will be included.
Events

```html
<!DOCTYPE html>
<html lang="en">
<head>
<meta charset="utf-8">
<title>Loudwave – Black Light Party</title>
<link rel="stylesheet" href="https://fonts.googleapis.com/css2?family=Source+Sans+3:wght@400;600&family=Audiowide&display=swap">
<style>
  :root {
    --bg-deep: #5a1448;
    --bg-mid: #a0246f;
    --bg-bright: #d8488e;
    --text-soft: #f7d6de;
    --text-warm: #f5c4c8;
    --text-white: #ffffff;
    --badge: #4a0f32;
    --ring: rgba(255, 255, 255, 0.35);
  }
  * { margin: 0; padding: 0; box-sizing: border-box; }
  html, body { width: 848px; height: 1200px; overflow: hidden; }
  body { font-family: "Source Sans 3", "Helvetica Neue", Arial, sans-serif; }

  .poster {
    position: relative;
    width: 848px;
    height: 1200px;
    overflow: hidden;
    background: var(--bg-mid);
  }
  .backdrop {
    position: absolute;
    inset: 0;
    background:
      radial-gradient(circle at 22% 20%, rgba(255,220,235,0.35) 0 90px, transparent 92px),
      radial-gradient(circle at 85% 17%, rgba(255,220,235,0.25) 0 55px, transparent 57px),
      radial-gradient(circle at 12% 52%, rgba(255,220,235,0.22) 0 55px, transparent 57px),
      radial-gradient(circle at 80% 62%, rgba(255,200,225,0.25) 0 110px, transparent 112px),
      radial-gradient(ellipse at 50% 40%, var(--bg-bright) 0%, var(--bg-mid) 45%, var(--bg-deep) 100%);
  }

  .headline { position: absolute; left: 0; right: 0; text-align: center; color: var(--text-soft); line-height: 1; }
  .location { top: 74px; font-size: 50px; letter-spacing: 1px; }
  .date { top: 130px; font-size: 68px; font-weight: 600; color: #fbe3e8; }
  .subtitle { top: 224px; font-size: 36px; }
  .title { top: 266px; font-size: 70px; }

  .badge { position: absolute; left: 0; top: 0; width: 848px; height: 1200px; }
  .brand-name {
    position: absolute;
    left: 0; right: 0;
    top: 550px;
    text-align: center;
    font-size: 60px;
    font-weight: 600;
    color: var(--text-white);
    line-height: 1;
    letter-spacing: 1px;
  }

  .dots { position: absolute; left: 313px; width: 222px; height: 6px; }
  .dots.top { top: 878px; }
  .dots.bottom { top: 994px; }

  .day { position: absolute; left: 0; right: 0; top: 893px; text-align: center; font-size: 46px; color: var(--text-soft); line-height: 1; }
  .hours { position: absolute; left: 0; right: 0; top: 950px; text-align: center; font-size: 33px; color: var(--text-warm); line-height: 1; }

  .contact { position: absolute; left: 36px; top: 1090px; font-family: "Audiowide", "Arial Black", sans-serif; color: var(--text-soft); font-size: 24px; line-height: 36px; }

  .corner-brand {
    position: absolute;
    right: 36px;
    top: 1104px;
    font-size: 24px;
    font-weight: 600;
    color: var(--text-white);
    line-height: 1;
  }
</style>
</head>
<body>
<main class="poster">
  <div class="backdrop" role="img" aria-label="Abstract magenta background with soft bokeh lights, thin crossing lines and paint specks"></div>

  <p class="headline location">LOCATION HERE</p>
  <p class="headline date">20.4.2015</p>
  <p class="headline subtitle">BLACK LIGHT</p>
  <p class="headline title">PARTY</p>

  <svg class="badge" viewBox="0 0 848 1200" aria-hidden="false">
    <circle cx="424" cy="584" r="217" fill="none" stroke="var(--ring)" stroke-width="2"/>
    <circle cx="424" cy="584" r="204" fill="var(--badge)" role="img" aria-label="Splash of music notes behind the event name"/>
  </svg>
  <p class="brand-name">loudwave</p>

  <svg class="dots top" viewBox="0 0 222 6" aria-hidden="true">
    <line x1="3" y1="3" x2="219" y2="3" stroke="#fff" stroke-width="5" stroke-linecap="round" stroke-dasharray="0 16.6"/>
  </svg>
  <p class="day">FRIDAY</p>
  <p class="hours">FROM 22:00 TO SUNRISE</p>
  <svg class="dots bottom" viewBox="0 0 222 6" aria-hidden="true">
    <line x1="3" y1="3" x2="219" y2="3" stroke="#fff" stroke-width="5" stroke-linecap="round" stroke-dasharray="0 16.6"/>
  </svg>

  <div class="contact">
    <p>CALL: 222-444-66</p>
    <p>WWW.LOUDWAVE-LIVE.COM</p>
  </div>

  <p class="corner-brand">loudwave</p>
</main>
</body>
</html>
```